A register your interest postcard

It is a slightly bigger postcard that wil be inserted inside a brochure. On one side it is to have the logo with the statement "at Quillory, Byron Bay" underneath. At the bottom it is to say "Register your interest to become an owner at The Harbourmark Circle. On the flipside it has the logo in a smaller version with again in smaller writing "Become an owner at The Harbourmark Circle". The main point of this side it to say " SMS your name to 0481 552 903 OR Name: Email: Phone:".
I would like a wood-look style postcard. It is for a luxury beach property that uses a lot of distressed wood in the building of the houses.
I would like a wood-look style postcard for a beach property.

```html
<!DOCTYPE html>
<html lang="en">
<head>
<meta charset="utf-8">
<title>Register Your Interest Postcard – The Harbourmark Circle</title>
<link rel="stylesheet" href="https://fonts.googleapis.com/css2?family=Roboto+Condensed:wght@300;400;700&display=swap">
<style>
  :root {
    --paper: #ffffff;
    --ink: #111111;
    --band: #000000;
    --wood-light: #8a5a2c;
    --wood-mid: #5a3a1e;
    --wood-dark: #2a1a0e;
    --night: #050403;
    --accent-orange: #e08a2a;
    --frost: rgba(225, 225, 220, 0.55);
    --white: #ffffff;
  }
  * { box-sizing: border-box; margin: 0; padding: 0; }
  html, body {
    width: 1200px; height: 651px; overflow: hidden;
    background: var(--paper);
    font-family: "Roboto Condensed", "Arial Narrow", sans-serif;
  }
  .canvas { position: relative; width: 1200px; height: 651px; }

  /* Front side */
  .front {
    position: absolute; left: 0; top: 0; width: 473px; height: 651px; overflow: hidden;
  }
  .front__wood {
    position: absolute; inset: 0;
    background:
      linear-gradient(180deg, rgba(0,0,0,0) 0%, rgba(0,0,0,0) 55%, rgba(5,4,3,0.85) 78%, var(--night) 90%),
      linear-gradient(90deg, var(--wood-dark) 0%, var(--wood-mid) 20%, var(--wood-light) 45%, var(--wood-mid) 70%, var(--wood-dark) 100%);
  }
  .mark-panel {
    position: absolute; left: 173px; top: 89px; width: 126px; height: 296px;
    border: 2px solid var(--accent-orange);
    background: var(--frost);
    display: flex; flex-direction: column; align-items: center;
    color: var(--ink);
  }
  .mark-panel__name {
    margin-top: 40px;
    font-weight: 700; font-size: 17px; line-height: 1.5;
    text-align: center; text-transform: uppercase; letter-spacing: 0.5px;
  }
  .mark-panel__place {
    margin-top: auto; margin-bottom: 8px;
    font-weight: 400; font-size: 14px; line-height: 16px;
    text-align: center; text-transform: uppercase; letter-spacing: 0.3px;
  }
  .front__brand {
    position: absolute; left: 45px; top: 545px;
    color: var(--white); font-weight: 700; font-size: 18px; line-height: 18px;
    text-transform: uppercase; letter-spacing: 0.5px;
  }
  .front__cta {
    position: absolute; right: 45px; top: 568px;
    color: var(--white); font-weight: 300; font-size: 14.5px; line-height: 17px;
    text-align: right;
  }

  /* Back side */
  .back { position: absolute; left: 473px; top: 0; width: 727px; height: 651px; }
  .mark-small {
    position: absolute; left: 214px; top: 206px; width: 73px; height: 171px;
    border: 1px solid var(--ink);
    display: flex; flex-direction: column; align-items: center; color: var(--ink);
  }
  .mark-small__name {
    margin-top: 22px;
    font-weight: 700; font-size: 10px; line-height: 1.6;
    text-align: center; text-transform: uppercase;
  }
  .mark-small__place {
    margin-top: auto; margin-bottom: 5px;
    font-size: 8.5px; line-height: 10px; text-align: center; text-transform: uppercase;
  }
  .divider { position: absolute; left: 401px; top: 131px; width: 2px; height: 320px; background: var(--ink); }
  .address-lines { position: absolute; left: 427px; top: 233px; width: 255px; }
  .address-lines span { display: block; height: 1px; background: var(--ink); margin-bottom: 28px; }

  .reply-band {
    position: absolute; left: 78px; top: 470px; width: 649px; height: 55px;
    background: var(--band); color: var(--white);
  }
  .reply-band__lead {
    position: absolute; left: 48px; top: 19px; font-size: 14.5px; font-weight: 300;
  }
  .reply-band__action {
    position: absolute; left: 330px; top: 7px; width: 285px;
    font-size: 17px; font-weight: 700; line-height: 20px; text-align: center;
  }
</style>
</head>
<body>
<main class="canvas">
  <section class="front">
    <div class="front__wood" role="img" aria-label="Photograph of weathered, distressed vertical timber planks fading to black at the bottom"></div>
    <div class="mark-panel">
      <div class="mark-panel__name">The<br>Harbourmark<br>Circle</div>
      <div class="mark-panel__place">At Quillory,<br>Byron Bay</div>
    </div>
    <div class="front__brand">The<br>Harbourmark<br>Circle</div>
    <p class="front__cta">Register your interest to become<br>an owner at The Harbourmark Circle</p>
  </section>

  <section class="back">
    <div class="mark-small">
      <div class="mark-small__name">The<br>Harbourmark<br>Circle</div>
      <div class="mark-small__place">At Quillory,<br>Byron Bay</div>
    </div>
    <div class="divider"></div>
    <div class="address-lines"><span></span><span></span><span></span><span></span><span></span></div>
    <div class="reply-band">
      <p class="reply-band__lead">Become an owner at The Harbourmark Circle</p>
      <p class="reply-band__action">SMS your name to 0481 552 903<br>OR Name: Email: Phone:</p>
    </div>
  </section>
</main>
</body>
</html>
```